Professional University Report Template

I have the need for a professionally-designed, multi-page report template, consisting of 8.5 x 11 inch pages - like a book, but not facing page design. An InDesign template would be best for my purposes.

This is a professional document in which I will need a main column for text, and a side column (around 1/3 of the width) to include photos, graphics, quotes, and lists. No background colors should be used, but perhaps some shading would be fine. This will be distributed as a PDF and will be printed by many in greyscale - so it should look great, and be easy to view without color.

As it is for a university publication, it must be overall professional and a bit subdued. The design should not overshadow the content, but enhance the overall experience. Most of all, I am aiming for something that is original and interesting.

Target Market(s)

University professors

Industry/Entity Type

University

Requirements
Must have
• Title page

Then a 3-page example document (use the text from sample indicator doc file):
Header 1 text
Header 2 text
body text
bulleted list
footer text noting the chapter title and page number

In the side columns of example pages (use the image files):
Photos
graphs
quoted text
bulleted list
Should not have
• No need for table of contents page, logo placement, or headers

```html
<!DOCTYPE html>
<html lang="en">
<head>
<meta charset="utf-8">
<title>Notable Indicator 2 — Enhancing Courses Through Service-Learning</title>
<link rel="stylesheet" href="https://fonts.googleapis.com/css2?family=Crimson+Pro:wght@600;700&display=swap">
<style>
  :root {
    --ink: #000000;
    --paper: #ffffff;
  }
  html, body {
    margin: 0;
    padding: 0;
    width: 927px;
    height: 1200px;
    overflow: hidden;
    background: var(--paper);
  }
  .title-page {
    position: relative;
    width: 927px;
    height: 1200px;
    background: var(--paper);
  }
  .title-art {
    position: absolute;
    left: 0;
    top: 0;
    width: 927px;
    height: 1200px;
    display: block;
  }
  .heading-word {
    font-family: "Crimson Pro", "Times New Roman", serif;
    font-weight: 700;
    fill: var(--ink);
  }
  .chapter-band {
    fill: var(--ink);
  }
  .chapter-subtitle {
    font-family: "Crimson Pro", "Times New Roman", serif;
    font-weight: 700;
    fill: var(--paper);
  }
  .chapter-numeral {
    font-family: "Crimson Pro", "Times New Roman", serif;
    font-weight: 700;
    fill: var(--ink);
  }
</style>
</head>
<body>
  <main class="title-page">
    <svg class="title-art" viewBox="0 0 927 1200" xmlns="http://www.w3.org/2000/svg" aria-labelledby="chapter-title">
      <title id="chapter-title">Notable Indicator 2: Enhancing Courses Through Service-Learning</title>
      <defs>
        <clipPath id="numeral-area">
          <rect x="342" y="626" width="505" height="491"/>
        </clipPath>
      </defs>

      <text class="heading-word heading-word--first" x="344" y="405" font-size="112" textLength="495" lengthAdjust="spacingAndGlyphs">NOTABLE</text>
      <text class="heading-word heading-word--second" x="344" y="500" font-size="80" textLength="497" lengthAdjust="spacingAndGlyphs">INDICATOR</text>

      <rect class="chapter-band" x="342" y="523" width="505" height="103"/>
      <text class="chapter-subtitle chapter-subtitle--main" x="366" y="570" font-size="40" textLength="452" lengthAdjust="spacingAndGlyphs">ENHANCING COURSES</text>
      <text class="chapter-subtitle chapter-subtitle--sub" x="374" y="609" font-size="29" textLength="442" lengthAdjust="spacingAndGlyphs">THROUGH SERVICE-LEARNING</text>

      <g clip-path="url(#numeral-area)">
        <text class="chapter-numeral" x="566" y="1117" font-size="780" textLength="281" lengthAdjust="spacingAndGlyphs">2</text>
      </g>
    </svg>
  </main>
</body>
</html>
```